Flyer Design Project

We are a storm restoration company that has recently begun restoration from water/flood damage from Hurricane Sandy. We provide disaster relief to homeowners and or commercial property owners after a flood. To start we offer cleanup and remediation which is taking out and disposing of all wet items in a home or business and the cutting out of walls, flooring and other items affected by a flood. We then provide remediation which includes the drying out of a home or business along with a dehumidifier to take all the moisture out of the air and to put it simply dry out the home. We also uses chemicals to clean and provide mold remediation to prevent to growth of mold. We work directly with a customers insurance company if they have flood insurance and after that we provide the services to rebuild and bring their property back to its condition before the storm.

Im looking for an informational type flier that I could insert into our business folders that we give to customers and also to use as fliers to pass out to potential customers. I want potential customers to look at this and feel comfortable with calling my company and working with us.

Company name Bellridge Building Partners. I attached our company logo.

Target Market(s)

Those affected by flooding from Hurricane Sandy

Industry/Entity Type

Insurance

Requirements
Must have
• Company logo, name and colors on flier
Nice to have
• Color photos that have to do with water restoration or showing flood damamge

```html
<!DOCTYPE html>
<html lang="en">
<head>
<meta charset="utf-8">
<title>Bellridge Building Partners – Flood Restoration Flyer</title>
<link rel="stylesheet" href="https://fonts.googleapis.com/css2?family=Open+Sans:wght@400;600;700&display=swap">
<style>
  :root{
    --navy:#0b2a4e;
    --navy-text:#13305a;
    --yellow:#f5ea45;
    --white:#ffffff;
    --rule:#d9cfc0;
    --edge:#e4e4e4;
  }
  *{box-sizing:border-box;margin:0;padding:0}
  html,body{width:1200px;height:900px;overflow:hidden;background:var(--white)}
  body{position:relative;font-family:"Open Sans",Arial,sans-serif;color:var(--navy-text)}
  .flyer{position:absolute;left:0;top:0;width:1200px;height:900px}
  .feature-panel{position:absolute;left:274px;top:36px;width:655px;height:544px;background:var(--navy)}
  .intro{position:absolute;color:var(--white);font-size:11.3px;line-height:12.6px;top:40px}
  .intro.left{left:38px;width:280px}
  .intro.right{left:345px;width:275px}
  .step{position:absolute;width:203px}
  .step-title{height:23px;background:var(--yellow);color:var(--navy);font-weight:700;font-size:16.5px;line-height:23px;padding-left:8px}
  .step-photo{position:relative;width:202px;height:113px}
  .step-copy{color:var(--white);font-size:8.9px;line-height:10.6px;margin-top:6px;width:200px}
  .step-1{left:71px;top:126px}
  .step-2{left:376px;top:126px}
  .step-3{left:71px;top:331px}
  .step-4{left:376px;top:331px}
  .photo-cleanup{background:linear-gradient(135deg,#6a5a48,#3f3a33 55%,#8a4a36)}
  .photo-dryout{background:linear-gradient(160deg,#1d2c44,#0f1a2b 60%,#2d4f4a)}
  .photo-mold{background:linear-gradient(135deg,#8a6a4a,#b89a7a 50%,#d8d2cc)}
  .photo-rebuild{background:linear-gradient(180deg,#6e9ad0 0%,#8fb3de 45%,#c89a6a 46%,#a8784c)}
  .photo-caption{position:absolute;left:2px;bottom:-1px;color:var(--white);font-weight:700;font-size:15px;opacity:.9}
  .brand{position:absolute;left:300px;top:630px;display:flex;align-items:center;gap:8px}
  .brand-mark{width:16px;height:16px;border-radius:50%;background:var(--navy)}
  .brand-name{font-weight:700;font-size:14px;line-height:17px;color:var(--navy);width:130px}
  .locations{position:absolute;top:600px;font-size:9px;line-height:10.5px;color:var(--navy-text)}
  .locations h3{font-size:11px;font-weight:700;line-height:14px;margin-bottom:1px}
  .locations p{margin-bottom:10.5px}
  .locations .group{margin-bottom:10px}
  .col-ny{left:468px}
  .col-mid{left:619px}
  .col-east{left:760px}
  .edge-right{position:absolute;left:928px;top:580px;width:1px;height:297px;background:var(--edge)}
  .rule-bottom{position:absolute;left:280px;top:876px;width:649px;height:1px;background:var(--rule)}
</style>
</head>
<body>
<div class="flyer">
  <section class="feature-panel">
    <p class="intro left">Integer gravida est quis orci congue quis porttitor libero luctus. Duis quis libero ut lorem malesuada malesuada nec eu mi. Nulla varius vestibulum mi, eu blandit risus lobortis non. Vivamus consequat scelerisque lorem at malesuada. .</p>
    <p class="intro right">dictum molestie sem, eu ornare justo euismod eget. Suspendisse id leo metus. Vestibulum ante ipsum primis in faucibus orci luctus et ultrices posuere cubilia Curae; Ut vehicula neque scelerisque ante rhoncus blandit. Vivamus tempus volutpat elit ut aliquam. Ut ut pharetra felis.</p>

    <article class="step step-1">
      <h2 class="step-title">1. Clean-up</h2>
      <div class="step-photo photo-cleanup" role="img" aria-label="Worker in a safety vest pumping floodwater out of a flooded stairwell with a green hose"></div>
      <p class="step-copy">Lorem ipsum dolor sit amet, consectetur adipiscing elit. Nullam quam ante, lobortis ac dapibus quis, vulputate vel nisi. Duis tristique, lacus a tincidunt volutpat, ipsum augue cursus libero, at pretium quam urna sed arcu..</p>
    </article>

    <article class="step step-2">
      <h2 class="step-title">2. Dry-out</h2>
      <div class="step-photo photo-dryout" role="img" aria-label="Technician carrying a green air mover past a dehumidifier inside a damp building"></div>
      <p class="step-copy">Donec iaculis pretium turpis, et egestas dui pharetra in. Donec lobortis lacus tortor, non pretium metus. Phasellus id enim dolor. Aenean vitae leo eu risus semper consequat.</p>
    </article>

    <article class="step step-3">
      <h2 class="step-title">3.&nbsp; Clean and De-mold</h2>
      <div class="step-photo photo-mold" role="img" aria-label="Worker in a protective suit and respirator testing a mold-covered wall">
        <span class="photo-caption">MOLD REMOVAL</span>
      </div>
      <p class="step-copy">Lorem ipsum dolor sit amet, consectetur adipiscing elit. Nullam quam ante, lobortis ac dapibus quis, vulputate vel nisi. Duis tristique, lacus a tincidunt volutpat, ipsum augue cursus libero, at pretium quam urna sed arcu..</p>
    </article>

    <article class="step step-4">
      <h2 class="step-title">4. Rebuild</h2>
      <div class="step-photo photo-rebuild" role="img" aria-label="Carpenters hammering a new wood wall frame under a blue sky"></div>
      <p class="step-copy">Donec iaculis pretium turpis, et egestas dui pharetra in. Donec lobortis lacus tortor, non pretium metus. Phasellus id enim dolor. Aenean vitae leo eu risus semper consequat.</p>
    </article>
  </section>

  <div class="brand">
    <span class="brand-mark"></span>
    <span class="brand-name">Bellridge Building Partners</span>
  </div>

  <div class="locations col-ny">
    <h3>New York Locations</h3>
    <p>Eastmoor<br>2140 Harbor Lane, Ste. 210<br>Eastmoor, NY 11900<br>Tel.: 555-622-0145</p>
    <p>Westfield Bay<br>118-04 Linden Row<br>Westfield Bay, NY 11902<br>Tel.: 555-279-0140<br>Fax: 555-279-0141</p>
    <p>Millbrook Falls<br>77 Orchard Ridge Rd., Ste. 500<br>Millbrook Falls, NY 10903<br>Tel.: 555-366-0196<br>Fax: 555-467-0101</p>
  </div>

  <div class="locations col-mid">
    <div class="group">
      <h3>Texas Locations</h3>
      Cedar Plains<br>240 West Prairie Road<br>Cedar Plains, Texas 75904<br>Tel.: 555-282-0160<br>Fax: 555-280-0168
    </div>
    <div class="group">
      <h3>Missouri Location</h3>
      Riverbend<br>14B Kessler Crossing<br>Riverbend Heights, MO 63905<br>Tel.: 555-205-0180<br>Fax: 555-205-0181
    </div>
    <div class="group">
      <h3>Virginia Location</h3>
      3300 Commons Parkway<br>Drive Suite. 100<br>Ashgrove, VA 20906<br>Tel.: 555-766-0134<br>Fax: 555-748-0142
    </div>
  </div>

  <div class="locations col-east">
    <div class="group">
      <h3>Kentucky Location</h3>
      Oakhaven<br>410 Meridian Circle, Ste. 100<br>Oakhaven, KY 40907<br>Tel.: 555-438-0133<br>Fax: 555-438-0132
    </div>
    <div class="group">
      <h3>Tennessee Location</h3>
      Ridgeport<br>815 Walnut Street, Ste. 600<br>Ridgeport, TN 37908
    </div>
  </div>

  <div class="edge-right"></div>
  <div class="rule-bottom"></div>
</div>
</body>
</html>
```